LVM IT Solutions Provider

Please read attached documentation completely before beginning Project. Thank you!

Mark Forge Project Requirements

Thank you for your interest in this design contest. We are always welcome to questions and are looking forward to seeing what you can come up with.

The logo is located on the current site homepage http://www.lumavex.com/

Bootstrap

We work on a Bootstrap platform with our custom built CMS. We require all designs to be

sized accordingly with the bootstrap grid system found here: http://getframelyn.com/css/#grid

Start of Competition Requirements

At the start of a competition, we are looking for general Home Page Design concepts and interior page design concepts as well.

HOME PAGE DESIGN

Any changes requested by the client in the original designs

Responsive Tablet View (using standard bootstrap media queries, we need to see an

example of a tablet size home page view)

Responsive Phone View (using standard bootstrap media queries, we need to see an

example of a phone size home page view)

INTERIOR PAGE DESIGN

These pages are general content pages. Our CMS allows for the creation of unlimited

pages and gives the client control of adding them. Interior Page Designs can be built

with 1 column, 2 columns (either right side bar or left sidebar)

Examples of buttons and button states,

Examples of drop down menus

Examples of H1 through H5 plus body copy

We uploaded a clean logo to use on the project. Thank you.

We added a updated Creative Brief document to help out. Please take a look thanks!

```html
<!DOCTYPE html>
<html lang="en">
<head>
<meta charset="utf-8">
<title>LVM – Technology Solutions</title>
<link rel="stylesheet" href="https://fonts.googleapis.com/css2?family=Nunito+Sans:wght@300;400;600;700;800&display=swap">
<style>
  :root {
    --brand-blue: #0d56a6;
    --link-blue: #1a5fae;
    --panel-blue: #0050a0;
    --gold: #f0b82c;
    --ink: #222;
    --body-grey: #555;
    --rule: #d9d9d9;
    --dark: #2c2c2c;
    --footer: #3e3e3e;
    --footer-text: #cfcfcf;
    --white: #fff;
  }
  * { box-sizing: border-box; margin: 0; padding: 0; }
  html, body { width: 1200px; height: 1100px; overflow: hidden; }
  body { font-family: "Nunito Sans", sans-serif; color: var(--ink); background: var(--white); position: relative; }

  .site-header { position: absolute; inset: 0 0 auto 0; height: 153px; background: linear-gradient(90deg, #fff 0%, #fff 25%, #f1f3f7 45%, #f6eef0 70%, #fff 100%); }
  .header-banner { position: absolute; left: 330px; top: 0; width: 800px; height: 153px; background: linear-gradient(100deg, rgba(200,210,230,0.35), rgba(240,200,205,0.35) 60%, rgba(255,255,255,0)); }
  .brand { position: absolute; left: 130px; top: 28px; display: flex; align-items: center; gap: 12px; }
  .brand-name { font-size: 56px; font-weight: 800; color: var(--brand-blue); letter-spacing: 1px; line-height: 1; }
  .brand-mark { width: 26px; height: 26px; border-radius: 50%; background: var(--gold); }

  .social { position: absolute; right: 130px; top: 23px; display: flex; align-items: center; gap: 7px; font-size: 12px; color: var(--brand-blue); }
  .social .label { margin-right: 6px; }
  .social .dot { width: 23px; height: 23px; border-radius: 50%; background: var(--link-blue); }
  .social .search { margin-left: 14px; }

  .main-nav { position: absolute; right: 130px; top: 100px; display: flex; font-size: 13px; color: #333; }
  .main-nav span { padding: 0 0 0 0; }
  .main-nav .sep { margin: 0 20px; color: #333; }
  .main-nav .active { color: var(--brand-blue); }

  .hero-band { position: absolute; left: 0; top: 153px; width: 1200px; height: 377px; background: var(--gold); }
  .slider { position: absolute; left: 130px; top: 137px; width: 941px; height: 374px; background: var(--white); border: 1px solid #ddd; padding: 4px; }
  .slide-image { width: 100%; height: 100%; background: linear-gradient(100deg, #0f1c2b 0%, #1d4655 40%, #2a3a40 70%, #6e6a5a 100%); position: relative; }
  .slide-caption { position: absolute; left: 0; top: 143px; width: 518px; height: 78px; background: rgba(255,255,255,0.88); padding: 3px 0 0 29px; font-size: 30px; line-height: 33px; font-weight: 400; color: #111; }
  .slider-dots { position: absolute; left: 428px; top: 331px; display: flex; gap: 7px; }
  .slider-dots i { width: 13px; height: 13px; border-radius: 50%; background: var(--white); display: block; }
  .slider-dots i.on { background: var(--gold); }

  .content { position: absolute; left: 131px; top: 547px; width: 611px; }
  .content h2 { font-size: 24px; font-weight: 400; color: var(--link-blue); margin-bottom: 10px; }
  .content p { font-size: 14px; line-height: 23px; color: var(--body-grey); }
  .content hr { border: 0; border-top: 1px solid var(--rule); margin: 28px 0 14px -1px; }
  .service-list { list-style: none; display: grid; grid-template-columns: 266px 300px; row-gap: 10px; margin-top: 20px; }
  .service-list li { font-size: 14.5px; color: var(--link-blue); display: flex; align-items: center; gap: 10px; height: 22px; }

  .hiring { position: absolute; left: 770px; top: 553px; width: 300px; height: 385px; background: var(--panel-blue); }
  .hiring h3 { height: 41px; background: var(--dark); color: var(--white); font-size: 18px; font-weight: 400; padding: 9px 21px; }
  .hiring ul { list-style: none; padding: 13px 0 0 21px; }
  .hiring li { font-size: 13.5px; color: var(--white); height: 36px; display: flex; align-items: center; }
  .hiring li::before { content: ""; width: 6px; height: 6px; border-radius: 50%; background: var(--gold); margin-right: 20px; }

  .site-footer { position: absolute; left: 0; top: 952px; width: 1200px; height: 148px; background: var(--footer); }
  .footer-brand { position: absolute; left: 130px; top: 22px; display: flex; align-items: center; gap: 8px; }
  .footer-brand .brand-name { font-size: 38px; color: #bfbfbf; }
  .footer-brand .brand-mark { width: 16px; height: 16px; background: #bfbfbf; }
  .partner { position: absolute; background: var(--white); }
  .copyright { position: absolute; left: 130px; top: 108px; font-size: 12px; color: var(--footer-text); }
  .footer-nav { position: absolute; right: 132px; top: 110px; display: flex; font-size: 11px; color: var(--footer-text); }
  .footer-nav .sep { margin: 0 18px; }
</style>
</head>
<body>
  <header class="site-header">
    <div class="header-banner" role="img" aria-label="Faint waving national flag decoration"></div>
    <div class="brand"><span class="brand-name">LVM</span><span class="brand-mark"></span></div>
    <div class="social">
      <span class="label">Follow Us:</span>
      <span class="dot" aria-label="Social profile"></span>
      <span class="dot" aria-label="Social profile"></span>
      <span class="dot" aria-label="Social profile"></span>
      <svg class="search" width="20" height="20" viewBox="0 0 20 20" aria-label="Search"><circle cx="7.5" cy="7.5" r="5.5" fill="none" stroke="#555" stroke-width="2"/><line x1="11.5" y1="11.5" x2="18" y2="18" stroke="#555" stroke-width="3" stroke-linecap="round"/></svg>
    </div>
    <nav class="main-nav">
      <span class="active">HOME</span><span class="sep">|</span>
      <span>ABOUT LVM</span><span class="sep">|</span>
      <span>DIVISIONS</span><span class="sep">|</span>
      <span>PRODUCTS &amp; SERVICES</span><span class="sep">|</span>
      <span>CONTACT US</span>
    </nav>
  </header>

  <div class="hero-band"></div>
  <section class="slider">
    <div class="slide-image" role="img" aria-label="Hands typing on a laptop before a digital security display, with an uniformed pilot beside it">
      <div class="slide-caption">Technology Solutions for National Defense &amp; Global Security</div>
      <div class="slider-dots"><i class="on"></i><i></i><i></i><i></i></div>
    </div>
  </section>

  <main class="content">
    <h2>Welcome to Our Website</h2>
    <p>Since 1988, LVM has been providing innovative and cost-effective products and services to customers worldwide. We are a vital source for leading-edge technology solutions that help our customers respond to opportunities faster, achieve more from their operations, and exceed their requirements.</p>
    <hr>
    <h2>Products &amp;&nbsp; Services</h2>
    <p>LVM provides the U.S. government and other customers with a vast array of quality products and services.</p>
    <ul class="service-list">
      <li><svg width="13" height="11" viewBox="0 0 13 11"><path d="M1 6l4 4 7-9" fill="none" stroke="#1a5fae" stroke-width="2.2"/></svg>Communication &amp; Networking</li>
      <li><svg width="13" height="11" viewBox="0 0 13 11"><path d="M1 6l4 4 7-9" fill="none" stroke="#1a5fae" stroke-width="2.2"/></svg>Intelligence &amp; Security</li>
      <li><svg width="13" height="11" viewBox="0 0 13 11"><path d="M1 6l4 4 7-9" fill="none" stroke="#1a5fae" stroke-width="2.2"/></svg>Technology Insertion</li>
      <li><svg width="13" height="11" viewBox="0 0 13 11"><path d="M1 6l4 4 7-9" fill="none" stroke="#1a5fae" stroke-width="2.2"/></svg>Automation System</li>
      <li><svg width="13" height="11" viewBox="0 0 13 11"><path d="M1 6l4 4 7-9" fill="none" stroke="#1a5fae" stroke-width="2.2"/></svg>Simulation &amp; Test</li>
      <li><svg width="13" height="11" viewBox="0 0 13 11"><path d="M1 6l4 4 7-9" fill="none" stroke="#1a5fae" stroke-width="2.2"/></svg>Cloud Solutions</li>
    </ul>
  </main>

  <aside class="hiring">
    <h3>WE ARE HIRING</h3>
    <ul>
      <li>A Career at LVM</li>
      <li>Benefits</li>
      <li>Corporate Culture</li>
      <li>How to Apply</li>
      <li>Job Search</li>
      <li>Recruiting Events</li>
      <li>Our Hiring Process</li>
      <li>Diversity</li>
      <li>Student Opportunities</li>
    </ul>
  </aside>

  <footer class="site-footer">
    <div class="footer-brand"><span class="brand-name">LVM</span><span class="brand-mark"></span></div>
    <div class="partner" style="left:805px;top:25px;width:86px;height:58px;" aria-label="Partner badge"></div>
    <div class="partner" style="left:908px;top:15px;width:79px;height:79px;" aria-label="Partner badge"></div>
    <div class="partner" style="left:995px;top:15px;width:70px;height:79px;" aria-label="Partner badge"></div>
    <div class="copyright">Copyright © 2014. All Right Reserved</div>
    <nav class="footer-nav">
      <span>HOME</span><span class="sep">|</span>
      <span>ABOUT LVM</span><span class="sep">|</span>
      <span>DIVISIONS</span><span class="sep">|</span>
      <span>PRODUCTS &amp; SERVICES</span><span class="sep">|</span>
      <span>CONTACT US</span>
    </nav>
  </footer>
</body>
</html>
```